Flyer DesignFESTIVE, FLORISTRY WORKSHOP

WE NEED A FLYER, TO SEND OUT TO PROSPECTIVE CUSTOMERS, TO ATTEND A ONE DAY CHRISTMAS WORKSHOP, ALL MATERIALS WILL BE SUPPLIED AND SO TO WE WILL PROVIDE REFRESHMENTS, PARTICIPIANTS JUST NEED TO BRING THIER FLORISTRY SCISSORS

ON THE DAY THE WILL PARTICIPIATE IN CREATING SEASONAL FLORISTRY DESIGNS THAT THEY CAN BRING HOME TO LAST THE FESTIVE SEASON,

MARGOT AND BEATRIX WILL BE THERE WITH SOME UNIQUE IDEAS TO ENHANCE OUR CHRISTMAS FESTIVITIES. TOTAL COST FOR THE DAY IS £79.00. AND THE DATE IS 6THDECEMBER, 2014, AT THE GILDEN LODGE HARWICK, WHICH HAS ALSO A BUS LINK TO MANY OTHER AREAS, SO ENJOY YOURSELVES, GET INTO THE FESTIVE FEELING ON THIS SPECIAL OCCASION

Target Market(s)

FLOWER LOVERS THAT LIKE TO CREATE THIER OWN FLORAL DESIGNS

Industry/Entity Type

Hotel

Font styles to use
Decorative

Requirements
Must have
• A CHRISTMAS ATMOSPHERE, WITH A BEAUTIFUL DOOR WREATH AND TABLE DESIGN

BOTH TUTORS ON THE DAY ARE HIGHLY SKILLED, HIGHLY QUALIFIED, WITH BEATRIX, HAVING WON NGW BRAMFORD MEDAL,
Nice to have
• BETTER WORDING THAN I HAVE GIVEN YOU

telephone number 02881430526

```html
<!DOCTYPE html>
<html lang="en">
<head>
<meta charset="utf-8">
<title>A One Day Christmas Workshop</title>
<link rel="stylesheet" href="https://fonts.googleapis.com/css2?family=Great+Vibes&family=Bodoni+Moda:wght@400;700;800&display=swap">
<style>
  :root {
    --page-bg: #ececec;
    --gold: #e9b93a;
    --gold-dark: #c9901c;
    --festive-red: #d11f2b;
    --festive-green: #0d6a33;
    --ink: #1e1e1e;
    --tree-green: #2f4a1c;
    --divider: #c9b98a;
  }
  * { margin: 0; padding: 0; box-sizing: border-box; }
  html, body {
    width: 1200px; height: 1000px; overflow: hidden;
    background: var(--page-bg);
  }
  .flyer {
    position: absolute;
    left: 24px; top: 92px;
    width: 960px; height: 680px;
    transform: scale(1.2);
    transform-origin: 0 0;
    overflow: hidden;
    box-shadow: 0 6px 18px rgba(0,0,0,0.25);
  }
  .flyer__photo {
    position: absolute; inset: 0;
    background:
      radial-gradient(ellipse at 50% 10%, rgba(216,178,74,0.55), transparent 55%),
      radial-gradient(ellipse at 10% 45%, rgba(230,200,120,0.5), transparent 35%),
      radial-gradient(ellipse at 92% 45%, rgba(200,140,50,0.55), transparent 35%),
      radial-gradient(ellipse at 8% 85%, rgba(168,20,29,0.9), transparent 35%),
      radial-gradient(ellipse at 95% 80%, rgba(168,20,29,0.85), transparent 30%),
      linear-gradient(180deg, #3d5a22 0%, var(--tree-green) 40%, #5a3a26 70%, #2a1a14 100%);
  }
  .flyer__frame { position: absolute; inset: 0; }
  .flyer__wreath {
    position: absolute;
    left: 76px; top: 42px;
    width: 144px; height: 162px;
    border-radius: 12px;
    background: radial-gradient(ellipse at 50% 50%, rgba(60,110,50,0.75), rgba(60,110,50,0.25) 70%, transparent 100%);
  }
  .content {
    position: absolute;
    left: 120px; width: 720px;
    text-align: center;
    font-family: "Bodoni Moda", "Didot", serif;
    font-size: 18px;
    line-height: 25px;
    color: var(--ink);
  }
  .title {
    top: 118px; left: 225px; width: 600px;
    font-family: "Great Vibes", cursive;
    font-weight: 400;
    font-size: 47px;
    line-height: 1;
    color: var(--festive-red);
    white-space: nowrap;
  }
  .intro { top: 209px; }
  .session { top: 273px; }
  .divider {
    position: absolute;
    left: 240px; top: 343px;
    width: 480px; height: 0;
    border-top: 1px dotted var(--divider);
  }
  .tutors { top: 354px; line-height: 28px; }
  .tutors__name {
    font-weight: 800;
    font-size: 30px;
    color: var(--festive-green);
  }
  .price {
    top: 425px;
    font-weight: 800;
    font-size: 26px;
    line-height: 30px;
    color: var(--festive-red);
  }
  .details { top: 458px; }
  .details__when {
    display: block;
    font-weight: 800;
    font-size: 14.5px;
    line-height: 22px;
    color: var(--festive-green);
    white-space: nowrap;
  }
</style>
</head>
<body>
  <article class="flyer">
    <div class="flyer__photo" role="img" aria-label="Photograph of a festive dinner table with wine glasses, red candle holders and napkins before a lit Christmas tree"></div>

    <svg class="flyer__frame" viewBox="0 0 960 680" aria-hidden="true">
      <defs>
        <linearGradient id="creamFill" x1="0" y1="0" x2="1" y2="1">
          <stop offset="0" stop-color="#fffef6"/>
          <stop offset="0.7" stop-color="#fffbe6"/>
          <stop offset="1" stop-color="#fbeebe"/>
        </linearGradient>
        <path id="framePath" d="M92 26
               Q150 80 240 80 L420 80 Q470 80 480 100 Q490 80 540 80 L760 80 Q850 80 872 26
               Q848 110 856 190 Q862 260 856 330 Q810 340 812 350 Q860 360 856 420 Q850 540 872 660
               Q820 590 700 590 L560 590 Q500 590 480 568 Q460 590 400 590 L240 590 Q150 592 92 660
               Q128 540 122 440 Q118 360 140 345 Q118 330 122 280 Q128 170 92 26 Z"/>
      </defs>
      <use href="#framePath" fill="url(#creamFill)" stroke="var(--gold)" stroke-width="9" stroke-linejoin="round"/>
      <use href="#framePath" fill="none" stroke="var(--gold-dark)" stroke-width="1.5"/>
    </svg>

    <div class="flyer__wreath" role="img" aria-label="Illustration of a pine door wreath with pine cones and a red bow"></div>

    <h1 class="content title">A One Day Christmas Workshop</h1>

    <p class="content intro">All materials will be supplied and so to we will provide<br>refreshments, participants just need to bring thier floristry scissors</p>

    <p class="content session">On the day the will participate in creating Seasonal Floristry<br>Designs that they can bring home to last the Festive Season</p>

    <div class="divider" aria-hidden="true"></div>

    <p class="content tutors"><span class="tutors__name">Margot</span> and <span class="tutors__name">Beatrix</span> will be there with some<br>unique ideas to enhance our Christmas Festivities.</p>

    <p class="content price">TOTAL COST FOR THE DAY IS £79</p>

    <p class="content details"><span class="details__when">AND THE DATE IS 6TH DECEMBER 2014, AT THE GILDEN LODGE HARWICK,</span>which has also a bus link to many other areas, so enjoy yourselves, get into<br>the festive feeling on this special occasion</p>
  </article>
</body>
</html>
```